Billboard design for retail kitchen cabinet business

We have a large 7,000 square-foot showroom of beautiful kitchen cabinet displays of all different designs and price ranges. In business for over 50 years with expert designers.
Full size Norvale Media 14' X 48' billboard
Target Market(s)
Retail public on high traffic Los Angeles streets

```html
<!DOCTYPE html>
<html lang="en">
<head>
<meta charset="utf-8">
<title>The Cabinet Hall – Billboard 14' x 48'</title>
<link rel="stylesheet" href="https://fonts.googleapis.com/css2?family=Barlow+Condensed:wght@400;600;700&display=swap">
<style>
  :root {
    --stage: #a3a3a3;
    --paper: #ffffff;
    --paper-shade: #ececec;
    --brand-yellow: #fbb614;
    --ink: #1c1c1c;
    --slate: #808080;
    --photo-light: #ece6dd;
    --photo-mid: #cdbba6;
    --photo-warm: #a77e5a;
  }
  * { margin: 0; padding: 0; box-sizing: border-box; }
  html, body {
    width: 993px; height: 1200px; overflow: hidden;
    background: var(--stage);
    font-family: "Barlow Condensed", "Arial Narrow", sans-serif;
  }
  .billboard {
    position: absolute; left: 40px; top: 467px;
    width: 913px; height: 266px;
    background: linear-gradient(115deg, var(--paper) 55%, var(--paper-shade) 100%);
    box-shadow: 6px 10px 14px rgba(0,0,0,0.45);
    overflow: hidden;
  }
  .billboard__art { position: absolute; inset: 0; }
  .tagline {
    position: absolute; left: 540px; top: 16px; width: 330px;
    text-align: center; color: var(--ink);
    font-weight: 400; font-size: 31px; line-height: 33px;
    text-transform: uppercase; letter-spacing: 0.2px;
  }
  .tagline strong { color: var(--brand-yellow); font-weight: 600; }
  .store-name {
    position: absolute; left: 520px; top: 144px; width: 370px;
    text-align: center; color: var(--brand-yellow);
    font-weight: 700; font-size: 52px; line-height: 52px;
    text-transform: uppercase;
  }
  .web-address {
    position: absolute; left: 420px; top: 238px; width: 260px;
    text-align: center; color: var(--paper);
    font-size: 21px; line-height: 28px; text-transform: uppercase;
  }
  .web-address b { font-weight: 600; }
  .phone {
    position: absolute; left: 728px; top: 216px; width: 170px; height: 40px;
    display: flex; align-items: center; gap: 8px;
    color: var(--paper); font-weight: 600; font-size: 27px;
  }
  .phone svg { width: 20px; height: 20px; }
</style>
</head>
<body>
  <section class="billboard">
    <svg class="billboard__art" viewBox="0 0 913 266" width="913" height="266">
      <defs>
        <linearGradient id="kitchen-tones" x1="0" y1="0" x2="1" y2="1">
          <stop offset="0" stop-color="var(--photo-light)"/>
          <stop offset="0.55" stop-color="var(--photo-mid)"/>
          <stop offset="1" stop-color="var(--photo-warm)"/>
        </linearGradient>
      </defs>
      <polygon class="kitchen-collage" points="21,0 432,0 507,127 375,266 21,266"
               fill="url(#kitchen-tones)" role="img"
               aria-label="Collage of bright kitchen showroom interiors with white cabinets and wood accents"/>
      <g class="collage-dividers" stroke="var(--paper)" stroke-width="5" fill="none">
        <line x1="21" y1="56" x2="230" y2="266"/>
        <line x1="216" y1="0" x2="110" y2="106"/>
        <line x1="110" y1="106" x2="236" y2="232"/>
        <line x1="265" y1="0" x2="400" y2="135"/>
        <line x1="400" y1="135" x2="270" y2="266"/>
        <line x1="236" y1="232" x2="355" y2="113"/>
        <line x1="148" y1="140" x2="275" y2="13"/>
        <line x1="400" y1="135" x2="480" y2="55"/>
      </g>
      <rect class="accent-bar" x="0" y="0" width="21" height="266" fill="var(--brand-yellow)"/>
      <polygon class="web-band" points="405,237 704,237 690,266 375,266" fill="var(--brand-yellow)"/>
      <polygon class="phone-panel" points="718,211 895,211 895,266 692,266" fill="var(--slate)"/>
      <rect class="end-tab" x="895" y="237" width="18" height="29" fill="var(--brand-yellow)"/>
    </svg>

    <p class="tagline">
      From <strong>Traditional Designs</strong><br>
      to the <strong>Latest Looks</strong> and<br>
      <strong>Styles</strong> you will find<br>
      exactly what you want at
    </p>
    <h1 class="store-name">The Cabinet Hall</h1>

    <p class="web-address">www.<b>thecabinethall</b>.net</p>

    <p class="phone">
      <svg viewBox="0 0 24 24" aria-hidden="true">
        <path fill="var(--brand-yellow)" d="M6.6 10.8a15.1 15.1 0 0 0 6.6 6.6l2.2-2.2c.3-.3.7-.4 1-.2 1.1.4 2.3.6 3.6.6.6 0 1 .4 1 1V20c0 .6-.4 1-1 1C10.6 21 3 13.4 3 4c0-.6.4-1 1-1h3.5c.6 0 1 .4 1 1 0 1.3.2 2.5.6 3.6.1.3 0 .7-.2 1z"/>
        <path fill="none" stroke="var(--brand-yellow)" stroke-width="1.8" stroke-linecap="round" d="M14 3.5a7 7 0 0 1 6.5 6.5M14 7a3.5 3.5 0 0 1 3 3"/>
      </svg>
      310.555.0148
    </p>
  </section>
</body>
</html>
```